Memento Mori Calendar

I’m looking for a graphic designer to create a Memento Mori–style life calendar that captures the essence of OLVENTRA — minimal, timeless, and deeply philosophical.

The design should be black and white only, with a refined, clean aesthetic and a sense of stillness and precision.
It should feel modern yet eternal, reflecting the themes of time, mortality, and presence.

Deliverables (Print-Ready Files):

24 x 30 in

24 x 32 in

24 x 36 in

A1 (594 x 841 mm)

All formats should be high-resolution and ready for professional printing (300 DPI, CMYK).

Design Requirements:

The calendar layout should follow the Memento Mori life calendar concept (weeks of life represented as small squares or circles).

The overall tone: minimal, meditative, monochrome.

Include the brand name: OLVENTRA (in an elegant, understated placement).

Add the following quote at the bottom or in a subtle position:

“Life can only be understood backwards; but it must be lived forwards.”
— Henrik Vastmoe

Target Market(s)

The OLVENTRA audience consists of urban, creative individuals aged 25 to 45, belonging to a middle to upper-middle income class. They lead conscious, quietly ambitious lives, seeking balance between inner depth and modern design. Their values center on awareness, presence, authenticity, and emotional depth, reflected in their preference for a monochrome, minimal, and timeless aesthetic. They tend to be introverted, reflective, and spiritually curious, drawn to brands that embody meaning and restraint rather than excess. Their cultural and stylistic affinities include Pyrel, Tulve, Ni Ostra, The Quiet Bench Guild, Durvanne, and Ombrix — labels that share OLVENTRAs devotion to simplicity, substance, and subtle ritual.

Font styles to use
Serif
Sans Serif

Colors

Designer to choose only greyscale colors for use in the design.

Requirements
Must have
• The calendar layout should follow the Memento Mori life calendar concept (weeks of life represented as small squares or circles). The overall tone: minimal, meditative, monochrome. Include the brand name: qrnvalto (in an elegant, understated placement). Add the following quote at the bottom or in a subtle position: “Life can only be understood backwards; but it must be lived forwards.” — Henrik Vastmoe

```html
<!DOCTYPE html>
<html lang="en">
<head>
<meta charset="utf-8">
<title>Life Calendar — OLVENTRA</title>
<link rel="stylesheet" href="https://fonts.googleapis.com/css2?family=Montserrat:wght@400;600;700&display=swap">
<style>
  :root {
    --paper: #ffffff;
    --ink: #0b0b0b;
  }
  * { margin: 0; padding: 0; box-sizing: border-box; }
  html, body {
    width: 960px;
    height: 1200px;
    overflow: hidden;
    background: var(--paper);
  }
  .poster {
    position: relative;
    width: 960px;
    height: 1200px;
    background: var(--paper);
    font-family: "Montserrat", sans-serif;
    color: var(--ink);
  }
  .life-wheel {
    position: absolute;
    left: 0;
    top: 0;
    width: 960px;
    height: 1060px;
  }
  .lived { fill: var(--ink); stroke: none; }
  .ahead { fill: var(--paper); stroke: var(--ink); stroke-width: 0.7; }
  .year-label {
    font-family: "Montserrat", sans-serif;
    font-size: 7px;
    font-weight: 400;
    fill: var(--ink);
    text-anchor: middle;
  }
  .year-label.major { font-size: 10.5px; font-weight: 700; }
  .birth-label {
    font-family: "Montserrat", sans-serif;
    font-size: 7px;
    font-weight: 600;
    fill: var(--ink);
    text-anchor: middle;
  }
  .birth-tick { stroke: var(--ink); stroke-width: 0.7; }
  .name-ring { fill: var(--paper); stroke: var(--ink); stroke-width: 1; }
  .brand-name {
    font-family: "Montserrat", sans-serif;
    font-weight: 600;
    font-size: 30px;
    letter-spacing: 1.5px;
    fill: var(--ink);
    text-anchor: middle;
    dominant-baseline: central;
  }
  .quote-band {
    position: absolute;
    left: 0;
    top: 1060px;
    width: 960px;
    height: 140px;
    background: var(--ink);
    color: var(--paper);
  }
  .quote-text {
    position: absolute;
    left: 0;
    top: 40px;
    width: 960px;
    text-align: center;
    font-size: 20px;
    font-weight: 400;
    letter-spacing: 0.2px;
  }
  .quote-author {
    position: absolute;
    right: 87px;
    top: 77px;
    font-size: 13px;
    font-weight: 400;
    letter-spacing: 0.3px;
  }
</style>
</head>
<body>
<main class="poster">
  <svg class="life-wheel" viewBox="0 0 960 1060" xmlns="http://www.w3.org/2000/svg">
    <defs>
      <g id="weeks-early">
        <circle cx="0" cy="-184" r="2.2"/>
        <circle cx="0" cy="-194.56" r="2.32"/>
        <circle cx="0" cy="-205.12" r="2.43"/>
        <circle cx="0" cy="-215.68" r="2.55"/>
        <circle cx="0" cy="-226.24" r="2.66"/>
        <circle cx="0" cy="-236.8" r="2.78"/>
        <circle cx="0" cy="-247.36" r="2.9"/>
        <circle cx="0" cy="-257.92" r="3.01"/>
        <circle cx="0" cy="-268.48" r="3.13"/>
        <circle cx="0" cy="-279.04" r="3.24"/>
        <circle cx="0" cy="-289.6" r="3.36"/>
        <circle cx="0" cy="-300.16" r="3.48"/>
        <circle cx="0" cy="-310.72" r="3.59"/>
        <circle cx="0" cy="-321.28" r="3.71"/>
        <circle cx="0" cy="-331.84" r="3.82"/>
        <circle cx="0" cy="-342.4" r="3.94"/>
        <circle cx="0" cy="-352.96" r="4.06"/>
        <circle cx="0" cy="-363.52" r="4.17"/>
        <circle cx="0" cy="-374.08" r="4.29"/>
        <circle cx="0" cy="-384.64" r="4.4"/>
      </g>
      <g id="weeks-late">
        <circle cx="0" cy="-395.2" r="4.52"/>
        <circle cx="0" cy="-405.76" r="4.64"/>
        <circle cx="0" cy="-416.32" r="4.75"/>
        <circle cx="0" cy="-426.88" r="4.87"/>
        <circle cx="0" cy="-437.44" r="4.98"/>
        <circle cx="0" cy="-448" r="5.1"/>
      </g>
      <g id="spoke">
        <use href="#weeks-early"/>
        <use href="#weeks-late"/>
      </g>
      <g id="year">
        <use href="#spoke"/>
        <use href="#spoke" transform="rotate(2.25)"/>
      </g>
      <g id="five-years">
        <use href="#year"/>
        <use href="#year" transform="rotate(4.5)"/>
        <use href="#year" transform="rotate(9)"/>
        <use href="#year" transform="rotate(13.5)"/>
        <use href="#year" transform="rotate(18)"/>
      </g>
    </defs>

    <!-- Week dots -->
    <g class="weeks" transform="translate(480 543)">
      <g class="lived">
        <use href="#five-years"/>
        <use href="#five-years" transform="rotate(22.5)"/>
        <use href="#five-years" transform="rotate(45)"/>
        <use href="#weeks-early" transform="rotate(67.5)"/>
      </g>
      <g class="ahead">
        <use href="#weeks-late" transform="rotate(67.5)"/>
        <use href="#spoke" transform="rotate(69.75)"/>
        <use href="#year" transform="rotate(72)"/>
        <use href="#year" transform="rotate(76.5)"/>
        <use href="#year" transform="rotate(81)"/>
        <use href="#year" transform="rotate(85.5)"/>
        <use href="#five-years" transform="rotate(90)"/>
        <use href="#five-years" transform="rotate(112.5)"/>
        <use href="#five-years" transform="rotate(135)"/>
        <use href="#five-years" transform="rotate(157.5)"/>
        <use href="#five-years" transform="rotate(180)"/>
        <use href="#five-years" transform="rotate(202.5)"/>
        <use href="#five-years" transform="rotate(225)"/>
        <use href="#five-years" transform="rotate(247.5)"/>
        <use href="#five-years" transform="rotate(270)"/>
        <use href="#five-years" transform="rotate(292.5)"/>
        <use href="#five-years" transform="rotate(315)"/>
        <use href="#five-years" transform="rotate(337.5)"/>
      </g>
    </g>

    <!-- Birth marker -->
    <text class="birth-label" x="480" y="68">Birth</text>
    <line class="birth-tick" x1="480" y1="73" x2="480" y2="87"/>

    <!-- Year labels -->
    <g class="year-labels" transform="translate(480 543)">
      <text class="year-label major" transform="rotate(2.25) translate(0 -462)">1</text>
      <text class="year-label" transform="rotate(6.75) translate(0 -462)">2</text>
      <text class="year-label" transform="rotate(11.25) translate(0 -462)">3</text>
      <text class="year-label" transform="rotate(15.75) translate(0 -462)">4</text>
      <text class="year-label major" transform="rotate(20.25) translate(0 -462)">5</text>
      <text class="year-label" transform="rotate(24.75) translate(0 -462)">6</text>
      <text class="year-label" transform="rotate(29.25) translate(0 -462)">7</text>
      <text class="year-label" transform="rotate(33.75) translate(0 -462)">8</text>
      <text class="year-label" transform="rotate(38.25) translate(0 -462)">9</text>
      <text class="year-label major" transform="rotate(42.75) translate(0 -462)">10</text>
      <text class="year-label" transform="rotate(47.25) translate(0 -462)">11</text>
      <text class="year-label" transform="rotate(51.75) translate(0 -462)">12</text>
      <text class="year-label" transform="rotate(56.25) translate(0 -462)">13</text>
      <text class="year-label" transform="rotate(60.75) translate(0 -462)">14</text>
      <text class="year-label major" transform="rotate(65.25) translate(0 -462)">15</text>
      <text class="year-label" transform="rotate(69.75) translate(0 -462)">16</text>
      <text class="year-label" transform="rotate(74.25) translate(0 -462)">17</text>
      <text class="year-label" transform="rotate(78.75) translate(0 -462)">18</text>
      <text class="year-label" transform="rotate(83.25) translate(0 -462)">19</text>
      <text class="year-label major" transform="rotate(87.75) translate(0 -462)">20</text>
      <text class="year-label" transform="rotate(92.25) translate(0 -462)">21</text>
      <text class="year-label" transform="rotate(96.75) translate(0 -462)">22</text>
      <text class="year-label" transform="rotate(101.25) translate(0 -462)">23</text>
      <text class="year-label" transform="rotate(105.75) translate(0 -462)">24</text>
      <text class="year-label major" transform="rotate(110.25) translate(0 -462)">25</text>
      <text class="year-label" transform="rotate(114.75) translate(0 -462)">26</text>
      <text class="year-label" transform="rotate(119.25) translate(0 -462)">27</text>
      <text class="year-label" transform="rotate(123.75) translate(0 -462)">28</text>
      <text class="year-label" transform="rotate(128.25) translate(0 -462)">29</text>
      <text class="year-label major" transform="rotate(132.75) translate(0 -462)">30</text>
      <text class="year-label" transform="rotate(137.25) translate(0 -462)">31</text>
      <text class="year-label" transform="rotate(141.75) translate(0 -462)">32</text>
      <text class="year-label" transform="rotate(146.25) translate(0 -462)">33</text>
      <text class="year-label" transform="rotate(150.75) translate(0 -462)">34</text>
      <text class="year-label major" transform="rotate(155.25) translate(0 -462)">35</text>
      <text class="year-label" transform="rotate(159.75) translate(0 -462)">36</text>
      <text class="year-label" transform="rotate(164.25) translate(0 -462)">37</text>
      <text class="year-label" transform="rotate(168.75) translate(0 -462)">38</text>
      <text class="year-label" transform="rotate(173.25) translate(0 -462)">39</text>
      <text class="year-label major" transform="rotate(177.75) translate(0 -462)">40</text>
      <text class="year-label" transform="rotate(182.25) translate(0 -462)">41</text>
      <text class="year-label" transform="rotate(186.75) translate(0 -462)">42</text>
      <text class="year-label" transform="rotate(191.25) translate(0 -462)">43</text>
      <text class="year-label" transform="rotate(195.75) translate(0 -462)">44</text>
      <text class="year-label major" transform="rotate(200.25) translate(0 -462)">45</text>
      <text class="year-label" transform="rotate(204.75) translate(0 -462)">46</text>
      <text class="year-label" transform="rotate(209.25) translate(0 -462)">47</text>
      <text class="year-label" transform="rotate(213.75) translate(0 -462)">48</text>
      <text class="year-label" transform="rotate(218.25) translate(0 -462)">49</text>
      <text class="year-label major" transform="rotate(222.75) translate(0 -462)">50</text>
      <text class="year-label" transform="rotate(227.25) translate(0 -462)">51</text>
      <text class="year-label" transform="rotate(231.75) translate(0 -462)">52</text>
      <text class="year-label" transform="rotate(236.25) translate(0 -462)">53</text>
      <text class="year-label" transform="rotate(240.75) translate(0 -462)">54</text>
      <text class="year-label major" transform="rotate(245.25) translate(0 -462)">55</text>
      <text class="year-label" transform="rotate(249.75) translate(0 -462)">56</text>
      <text class="year-label" transform="rotate(254.25) translate(0 -462)">57</text>
      <text class="year-label" transform="rotate(258.75) translate(0 -462)">58</text>
      <text class="year-label" transform="rotate(263.25) translate(0 -462)">59</text>
      <text class="year-label major" transform="rotate(267.75) translate(0 -462)">60</text>
      <text class="year-label" transform="rotate(272.25) translate(0 -462)">61</text>
      <text class="year-label" transform="rotate(276.75) translate(0 -462)">62</text>
      <text class="year-label" transform="rotate(281.25) translate(0 -462)">63</text>
      <text class="year-label" transform="rotate(285.75) translate(0 -462)">64</text>
      <text class="year-label major" transform="rotate(290.25) translate(0 -462)">65</text>
      <text class="year-label" transform="rotate(294.75) translate(0 -462)">66</text>
      <text class="year-label" transform="rotate(299.25) translate(0 -462)">67</text>
      <text class="year-label" transform="rotate(303.75) translate(0 -462)">68</text>
      <text class="year-label" transform="rotate(308.25) translate(0 -462)">69</text>
      <text class="year-label major" transform="rotate(312.75) translate(0 -462)">70</text>
      <text class="year-label" transform="rotate(317.25) translate(0 -462)">71</text>
      <text class="year-label" transform="rotate(321.75) translate(0 -462)">72</text>
      <text class="year-label" transform="rotate(326.25) translate(0 -462)">73</text>
      <text class="year-label" transform="rotate(330.75) translate(0 -462)">74</text>
      <text class="year-label major" transform="rotate(335.25) translate(0 -462)">75</text>
      <text class="year-label" transform="rotate(339.75) translate(0 -462)">76</text>
      <text class="year-label" transform="rotate(344.25) translate(0 -462)">77</text>
      <text class="year-label" transform="rotate(348.75) translate(0 -462)">78</text>
      <text class="year-label" transform="rotate(353.25) translate(0 -462)">79</text>
      <text class="year-label major" transform="rotate(357.75) translate(0 -462)">80</text>
    </g>

    <!-- Centre name -->
    <g class="centre-name">
      <circle class="name-ring" cx="480" cy="540" r="150"/>
      <text class="brand-name" x="480" y="540">OLVENTRA</text>
    </g>
  </svg>

  <footer class="quote-band">
    <p class="quote-text">“Life can only be understood backwards; but it must be lived forwards.”</p>
    <p class="quote-author">- Henrik Vastmoe</p>
  </footer>
</main>
</body>
</html>
```